IT Company requires new Business Card design.

Over the years we have had a few different business card designs. We are now due for new cards across the board for all staff. We felt this would be a good time to start fresh with a new design. Our traditional card simply had our details on the front, and a list of services on the back. We don't particularly need the list of services, we have had cards where the only thing on the rear of the card was our logo.
Feel free to be creative, we would like our tag line "Complete IT Management" to appear at some point, doesn't necessarily have to be with the logo.
I have attached samples and drafts of various previous cards we have used over the years.
Industry/Entity Type
Business
Look and feel
Each slider illustrates characteristics of the customer's brand and the style your logo design should communicate.

```html
<!DOCTYPE html>
<html lang="en">
<head>
<meta charset="utf-8">
<title>Ridgeline Networking – Business Card</title>
<link rel="stylesheet" href="https://fonts.googleapis.com/css2?family=Open+Sans:wght@300;400;700&display=swap">
<style>
  :root {
    --card-bg: #f1f1f1;
    --brand-blue: #1565a8;
    --brand-slate: #5f7282;
    --text-dark: #3a3a3a;
  }
  * { margin: 0; padding: 0; box-sizing: border-box; }
  html, body {
    width: 1200px;
    height: 669px;
    overflow: hidden;
    background: var(--card-bg);
  }
  .card {
    position: relative;
    width: 1200px;
    height: 669px;
    background: var(--card-bg);
    font-family: "Open Sans", sans-serif;
    color: var(--text-dark);
  }
  .rule {
    position: absolute;
    top: 245px;
    height: 20px;
    background: var(--brand-blue);
  }
  .rule--left  { left: 0; width: 34px; }
  .rule--main  { left: 540px; width: 600px; }
  .rule--right { left: 1181px; width: 19px; }

  .brand {
    position: absolute;
    left: 92px;
    top: 207px;
    display: flex;
    align-items: center;
    gap: 16px;
  }
  .brand__mark {
    width: 96px;
    height: 96px;
    background: var(--brand-slate);
  }
  .brand__name {
    font-weight: 700;
    font-size: 26px;
    line-height: 34px;
    color: var(--brand-blue);
    white-space: nowrap;
  }
  .brand__tagline {
    margin-top: 4px;
    font-weight: 400;
    font-size: 16px;
    line-height: 22px;
    color: var(--text-dark);
  }

  .person {
    position: absolute;
    right: 59px;
    top: 100px;
    text-align: right;
    color: var(--brand-blue);
  }
  .person__name {
    font-weight: 700;
    font-size: 36px;
    line-height: 44px;
  }
  .person__role {
    font-weight: 400;
    font-size: 29px;
    line-height: 38px;
  }

  .contact {
    position: absolute;
    left: 700px;
    top: 326px;
    font-weight: 300;
    font-size: 25px;
    line-height: 40px;
  }
  .contact__address { margin-bottom: 38px; }
  .contact__label {
    display: inline-block;
    width: 40px;
  }
  .contact__web { margin-top: 30px; }
</style>
</head>
<body>
  <main class="card">
    <div class="rule rule--left"></div>
    <div class="rule rule--main"></div>
    <div class="rule rule--right"></div>

    <div class="brand">
      <div class="brand__mark"></div>
      <div class="brand__text">
        <div class="brand__name">Ridgeline Networking</div>
        <div class="brand__tagline">Complete IT Management</div>
      </div>
    </div>

    <div class="person">
      <div class="person__name">DANIEL CARTER</div>
      <div class="person__role">Position</div>
    </div>

    <div class="contact">
      <p class="contact__address">12 / 37 Marlowe Way, Kestrel Park, 6170</p>
      <p><span class="contact__label">P:</span>08 9555 0140; F: 08 9555 0142</p>
      <p><span class="contact__label">M:</span>0400 555 218</p>
      <p><span class="contact__label">E:</span>daniel@ridgelinenetworking.com.au</p>
      <p class="contact__web">www.ridgelinenetworking.com.au</p>
    </div>
  </main>
</body>
</html>
```